Tourism Marketing needing sleek, clear design for business card & proposal documents.

***Company background***
"Quiet Harbour" is a company specializing in tourism marketing and project management. We do international wholesale, event management as well as ongoing representation of tourism and hospitality companies.

***Target market***
We cater to tourism companies and hotel professionals.

***Task***
We would like to get a single sided business card designed (but will still consider two sided, we are open to any ideas you may have). The layout for this card should be modern and elegant. Currently we do not have a logo, but we would like our business name in a really simple typography for the business card (similar to Moonrise Palace's logo - www.moonrisepalace-example.com.au).We are after a design that is clear, strong enough to be recognised as Quiet Harbour that does not require any fancy design. Another option is a simple play on QH (Quiet Harbour) or simply have Quiet Harbour featured elsewhere on card more as a brand/logo.

Feel free to submit different fonts if you feel you have any other fonts/designs that may be suitable for this card other than sans serifs. Should this project be successful, we will be considering several other projects for business proposal templates and eventually a website design.

The information that needs to go on the card are as follows:

Marta Holloway
Director
Quiet Harbour
Tourism Marketing & Representation
87 Wendover Parade
Prahran, Victoria, 3181 Australia
T +61 498203617 E marta@quietharbour-example.com.au

***Look and feel***
We'd like the business card design to express the following:
Modern, sleek, elegant, simple, discreet, quality, subtle, professional, creative, innovation

In terms of typography, we like something really simple and blocky (similar font to Moonrise Palace's logo - www.moonrisepalace-example.com.au)

***Colour scheme***
Shades of grey and dark teal

***Note***
Although our main target market are professionals, we would like the business card design to be versatile enough to be used outside of the tourism industry and need to appeal to different markets.

I do not have existing logo. Was hoping for a design that may be clear, strong enough not to require one. Other option is a simple play on QH (Quiet Harbour) or simply have Quiet Harbour featured elsewhere on card more as a brand/logo.

Marta Holloway
Director
Quiet Harbour Pty Ltd 
87 Wendover Parade
T +61 498203617  E  marta@quietharbour-example.com.au

Thank you for designs so far. Many have used a mauve colour which matches our company profile. This is not necessary, as that is just a draft and will be completely redesigned, so dont  feel you need to incorporate the mauve.

My colour preferences are for a white or grey background, and I like fonts in dark teals, grey or other sophisticated but modern colours. feel free to submit different fonts if you you have other fonts you thing would be suitable for this card, along with sans serifs. Should this project be successful, we will be considering several others for business proposal templates and eventually website. 

Target Market(s)

International Hospitality Senior Executives, Directors of International Tourism Companies, Directors of Tourism Bodies Internationally, local Tourism

Industry/Entity Type

Hospitality

Requirements
Should not have
• must not have bright garish colour, swirly patterns or anything that dates too much.

```html
<!DOCTYPE html>
<html lang="en">
<head>
<meta charset="utf-8">
<title>Quiet Harbour – Business Card</title>
<link rel="stylesheet" href="https://fonts.googleapis.com/css2?family=Jost:wght@500&family=Arimo:wght@400;700&display=swap">
<style>
  :root {
    --brand-blue: #0e65ab;
    --grey-light: #e6e6e6;
    --grey-mid: #d2d2d2;
    --grey-dark: #a9a9a9;
    --text-grey: #6b6e72;
    --white: #ffffff;
    --page: #ffffff;
  }
  * { margin: 0; padding: 0; box-sizing: border-box; }
  html, body {
    width: 1200px;
    height: 900px;
    overflow: hidden;
    background: var(--page);
  }
  .canvas {
    position: relative;
    width: 1200px;
    height: 900px;
  }
  .business-card {
    position: absolute;
    left: 176px;
    top: 188px;
    width: 848px;
    height: 518px;
    background: var(--brand-blue);
    overflow: hidden;
  }
  .card-header {
    position: absolute;
    left: 0;
    top: 0;
    width: 100%;
    height: 258px;
    background: linear-gradient(to bottom, var(--grey-light) 0%, var(--grey-light) 28%, var(--grey-mid) 62%, var(--grey-dark) 100%);
  }
  .brand-name {
    position: absolute;
    left: 67px;
    top: 36px;
    font-family: "Jost", sans-serif;
    font-weight: 500;
    font-size: 58px;
    line-height: 60px;
    letter-spacing: 1px;
    color: var(--brand-blue);
    text-transform: uppercase;
  }
  .brand-tagline {
    position: absolute;
    left: 67px;
    top: 168px;
    font-family: "Arimo", sans-serif;
    color: var(--text-grey);
  }
  .brand-tagline .tagline-primary {
    display: block;
    font-size: 27.5px;
    line-height: 32px;
    font-weight: 400;
  }
  .brand-tagline .tagline-secondary {
    display: block;
    font-size: 26px;
    line-height: 32px;
    font-weight: 700;
    letter-spacing: 4.5px;
  }
  .person {
    position: absolute;
    right: 45px;
    top: 214px;
    text-align: right;
  }
  .person-name {
    font-family: "Jost", sans-serif;
    font-weight: 500;
    font-size: 48px;
    line-height: 48px;
    letter-spacing: 1.5px;
    color: var(--brand-blue);
    white-space: nowrap;
  }
  .person-title {
    margin-top: 4px;
    font-family: "Arimo", sans-serif;
    font-weight: 700;
    font-size: 29px;
    line-height: 34px;
    color: var(--white);
  }
  .contact-details {
    position: absolute;
    left: 66px;
    top: 347px;
    font-family: "Arimo", sans-serif;
    font-size: 29px;
    line-height: 35px;
    color: var(--white);
    list-style: none;
  }
  .contact-details .contact-address { font-weight: 700; }
</style>
</head>
<body>
  <main class="canvas">
    <article class="business-card">
      <header class="card-header">
        <div class="brand-name">Quiet<br>Harbour</div>
        <p class="brand-tagline">
          <span class="tagline-primary">Tourism &amp; Marketing</span>
          <span class="tagline-secondary">Representation</span>
        </p>
      </header>
      <div class="person">
        <h1 class="person-name">MARTA HOLLOWAY</h1>
        <p class="person-title">DIRECTOR</p>
      </div>
      <ul class="contact-details">
        <li class="contact-address">87 Wendover Parade</li>
        <li class="contact-locality">Prahran, Victoria, 3181 Australia</li>
        <li class="contact-phone">T +61 498203617</li>
        <li class="contact-email">E marta@quietharbour-example.com.au</li>
      </ul>
    </article>
  </main>
</body>
</html>
```